Mabel's Fitness Business Cards

I would like my business cards to look expensive and sophisticated using my logo and the information below.

FRONT
Mabel’s Fitness logo

Tag line Become your happiest, healthiest and strongest self

Mabel Quint Harlow
Personal Trainer

e. mabel@mabelsfitstudio.example

t. 0781530462

w. www.mabelsfitstudio.example

```html
<!DOCTYPE html>
<html lang="en">
<head>
<meta charset="utf-8">
<title>Mabel's Fitness Business Cards</title>
<link href="https://fonts.googleapis.com/css2?family=Open+Sans:ital,wght@0,400;0,600;1,400&display=swap" rel="stylesheet">
<style>
  :root {
    --backdrop: #2e2e30;
    --card-dark: #1e191d;
    --card-light: #fbfbfb;
    --teal: #5fa9b4;
    --taupe: #8a7f7d;
    --ink: #6d6768;
    --divider: #8c8280;
  }
  * { margin: 0; padding: 0; box-sizing: border-box; }
  html, body { width: 1200px; height: 900px; overflow: hidden; }
  body {
    background: var(--backdrop);
    font-family: "Open Sans", Arial, sans-serif;
    position: relative;
  }
  .card {
    position: absolute;
    left: 285px;
    width: 630px;
    height: 360px;
    border-radius: 22px;
  }
  .card-back { top: 70px; background: var(--card-dark); }
  .card-front { top: 470px; background: var(--card-light); }

  .brand {
    display: flex;
    flex-direction: column;
    align-items: center;
    gap: 14px;
  }
  .brand-dot {
    width: 58px; height: 58px;
    border-radius: 50%;
    border: 4px solid var(--teal);
  }
  .brand-name {
    color: var(--teal);
    font-weight: 400;
    text-transform: uppercase;
    letter-spacing: 0.32em;
    font-size: 22px;
    text-align: center;
    line-height: 1.3;
  }
  .card-back .brand {
    position: absolute;
    left: 0; right: 0; top: 108px;
  }
  .card-front .brand {
    position: absolute;
    left: 48px; top: 92px; width: 240px;
  }
  .card-front .brand-name { font-size: 20px; }

  .divider {
    position: absolute;
    left: 318px; top: 66px;
    width: 1px; height: 170px;
    background: var(--divider);
  }
  .contact {
    position: absolute;
    left: 350px; top: 62px;
  }
  .contact-name {
    color: var(--teal);
    font-size: 16px;
    letter-spacing: 0.03em;
    text-transform: uppercase;
  }
  .contact-role {
    color: var(--ink);
    font-size: 15px;
    margin: 2px 0 12px 8px;
  }
  .contact-list { list-style: none; margin-left: 14px; }
  .contact-list li {
    display: flex; align-items: center; gap: 8px;
    color: var(--ink);
    font-size: 15px;
    line-height: 25px;
  }
  .contact-icon { width: 14px; height: 14px; flex: none; }
  .tagline {
    position: absolute;
    left: 0; right: 0; bottom: 46px;
    text-align: center;
    color: var(--taupe);
    font-style: italic;
    font-size: 17px;
  }
</style>
</head>
<body>
  <section class="card card-back" aria-label="Card back">
    <div class="brand">
      <span class="brand-dot"></span>
      <span class="brand-name">Mabel’s Fitness</span>
    </div>
  </section>

  <section class="card card-front" aria-label="Card front">
    <div class="brand">
      <span class="brand-dot"></span>
      <span class="brand-name">Mabel’s Fitness</span>
    </div>
    <div class="divider"></div>
    <div class="contact">
      <p class="contact-name">Mabel Quint Harlow</p>
      <p class="contact-role">Personal Trainer</p>
      <ul class="contact-list">
        <li>
          <svg class="contact-icon" viewBox="0 0 14 14" aria-hidden="true">
            <circle cx="7" cy="7" r="7" fill="#5fa9b4"/>
            <path d="M4.5 3.8l1.3-.3.8 1.8-.8.6a5 5 0 0 0 2.3 2.3l.6-.8 1.8.8-.3 1.3c-3 .2-5.9-2.7-5.7-5.7z" fill="#fff"/>
          </svg>
          0781530462
        </li>
        <li>
          <svg class="contact-icon" viewBox="0 0 14 14" aria-hidden="true">
            <circle cx="7" cy="7" r="7" fill="#5fa9b4"/>
            <rect x="3.5" y="4.5" width="7" height="5" fill="#fff"/>
            <path d="M3.5 4.7L7 7.3l3.5-2.6" fill="none" stroke="#5fa9b4" stroke-width=".8"/>
          </svg>
          mabel@mabelsfitstudio.example
        </li>
        <li>
          <svg class="contact-icon" viewBox="0 0 14 14" aria-hidden="true">
            <circle cx="7" cy="7" r="7" fill="#5fa9b4"/>
            <circle cx="7" cy="7" r="3.6" fill="none" stroke="#fff" stroke-width=".9"/>
            <path d="M3.4 7h7.2M7 3.4c-1.6 2-1.6 5.2 0 7.2M7 3.4c1.6 2 1.6 5.2 0 7.2" fill="none" stroke="#fff" stroke-width=".7"/>
          </svg>
          www.mabelsfitstudio.example
        </li>
      </ul>
    </div>
    <p class="tagline">Become your happiest, healthiest and strongest self</p>
  </section>
</body>
</html>
```